OurPlume Lifting Hope across a trusted circle

I am looking for a sleek, clean and simple app design. I need also a payment page and offering different packages and payment types.

I would like the color scheme to be black or white very futuristic like the movie q-lantern.

The profile page displaying the picture, as clean and future like as possible.

Share profile options, manage subscription, update profile, help ect….

On the verified page last one, the social media logos are interactive so the user can share their info through the connected social media account.

Target Market(s)

Professionals and individuals.

Industry/Entity Type

Due diligence & background checks verification

Font styles to use
Sans Serif

Colors
0054AA
0677BA
7BADD7
CADEEF
E8F1F8
0094D4
00A9DD
6FCCEA
C7EBF8
E9F6FB
59FF00
82FF00
B8FF75
E3FFCB
F4FFEA

Requirements
Must have
• The ability to add my social media links or log in through the app directly for direct confirmation. After email entered on account sign up they get either a confirmation email or a text through telephone number verification.
Nice to have
• Account creation to add profile picture must take a selfie.

```html
<!DOCTYPE html>
<html lang="en">
<head>
<meta charset="utf-8">
<title>OurPlume – Sign in and account creation</title>
<link rel="stylesheet" href="https://fonts.googleapis.com/css2?family=Inter:wght@400;500;600&display=swap">
<style>
  :root{
    --page:#ffffff;
    --screen-top:#2d4159;
    --screen-bottom:#161b21;
    --text:#ffffff;
    --text-soft:#c9d2dc;
    --text-muted:#8d98a5;
    --field-border:#5b6878;
    --field-active:#0677BA;
    --brand:#0054AA;
    --accent:#0094D4;
    --link:#00A9DD;
    --tick:#6FCCEA;
    --note-bg:#1d2126;
    --note-rule:#3a4048;
    --step-idle:#1f3a5c;
  }
  *{box-sizing:border-box;margin:0;padding:0}
  html,body{width:1200px;height:647px;overflow:hidden;background:var(--page)}
  body{position:relative;font-family:"Inter",sans-serif;color:var(--text)}
  .screen{
    position:absolute;top:76px;width:228px;height:500px;border-radius:26px;overflow:hidden;
    background:linear-gradient(180deg,var(--screen-top) 0%,#1f2a37 55%,var(--screen-bottom) 100%);
  }
  .screen--login{left:110px}
  .screen--details{left:363px}
  .screen--username{left:609px}
  .screen--credentials{left:861px}
  .screen > *{position:absolute}

  .status-time{left:14px;top:15px;font-size:9.5px;font-weight:600}
  .status-icons{right:14px;top:16px}
  .back{left:15px;top:44px}
  .title{left:16px;top:68px;font-size:19.5px;font-weight:400;line-height:24px;letter-spacing:-.1px}
  .brand{left:150px;top:88px;display:flex;align-items:center;gap:3px;font-size:8px;font-weight:600}
  .brand-dot{width:9px;height:9px;border-radius:50%;background:var(--accent)}
  .progress{left:16px;top:127px;display:flex;gap:5px}
  .progress span{height:3px;border-radius:2px;background:var(--accent)}
  .progress span:first-child{width:37px}
  .progress span:last-child{width:6px}

  .field{
    left:22px;width:185px;height:31px;border:1px solid var(--field-border);border-radius:16px;
    display:flex;align-items:center;padding:0 13px;font-size:9px;color:var(--text-muted);
  }
  .field--wide{left:27px;width:175px}
  .field--active{border-color:var(--field-active);color:var(--text)}
  .field--filled{color:var(--text)}
  .field .icon-lead{display:flex;align-items:center;padding-right:7px;margin-right:7px;border-right:1px solid var(--field-border);height:12px}
  .field .icon-trail{margin-left:auto;display:flex}
  .caret{display:inline-block;width:1px;height:10px;background:var(--text);margin-left:1px;vertical-align:middle}
  .mask{letter-spacing:1px;font-size:7px;color:var(--text-soft)}

  .link{color:var(--link);text-decoration:underline;font-size:7.5px}
  .forgot{right:28px;top:240px}
  .button{
    left:19px;width:189px;height:31px;border-radius:16px;background:var(--brand);
    display:flex;align-items:center;justify-content:center;gap:5px;font-size:9.5px;font-weight:600;
  }
  .screen--login .button{left:22px;width:185px}
  .divider{left:28px;width:172px;top:330px;display:flex;align-items:center;gap:10px;font-size:7.5px;color:var(--text-muted)}
  .divider::before,.divider::after{content:"";flex:1;height:1px;background:#323c48}
  .scan-label{left:0;width:100%;top:355px;text-align:center;font-size:8.5px;color:var(--text-soft)}
  .scan-icon{left:101px;top:371px}
  .signup-prompt{left:0;width:100%;top:462px;text-align:center;font-size:7.5px;color:var(--text-muted)}

  .stepper{left:30px;width:168px;top:160px;height:40px}
  .stepper > *{position:absolute}
  .step-line{top:11px;height:1px;background:#3d4b5c}
  .step-line--done{background:var(--accent)}
  .step-current{width:22px;height:22px;border-radius:50%;background:var(--brand);border:2px solid #1b3f6a;
    display:flex;align-items:center;justify-content:center;font-size:8.5px;font-weight:600;top:0}
  .step-idle{width:12px;height:12px;border-radius:50%;background:var(--step-idle);top:5px;
    display:flex;align-items:center;justify-content:center;font-size:5.5px;color:#8fb3d8}
  .step-done{top:3px}
  .step-label{top:26px;font-size:7px;color:var(--text-soft);text-align:center;line-height:9px;width:60px}

  .lead{left:0;width:100%;text-align:center;font-size:7.5px;color:var(--text-soft);line-height:10px}
  .note{
    left:27px;width:175px;border-radius:5px;background:var(--note-bg);font-size:6.6px;color:var(--text-soft);
  }
  .note-inline{top:376px;height:23px;display:flex;align-items:center;gap:5px;padding:0 8px}
  .note-inline strong{font-weight:500;color:var(--text)}
  .note-block{padding:13px 12px 10px}
  .note-head{display:flex;align-items:center;gap:5px;font-size:7.5px;color:var(--text);padding:0 0 5px 2px;border-bottom:1px solid var(--note-rule);margin-bottom:6px}
  .note-body{padding:0 6px 0 14px;line-height:9.5px}
  .privacy{left:27px;width:180px;top:407px;display:flex;gap:6px;font-size:6.2px;line-height:8.5px;color:var(--text-muted)}
  .privacy .link{font-size:6.2px}
  .privacy-icon{flex:none;width:14px;height:14px;border-radius:50%;background:var(--brand);display:flex;align-items:center;justify-content:center;margin-top:1px}
</style>
</head>
<body>

<svg width="0" height="0" style="position:absolute" aria-hidden="true">
  <defs>
    <g id="status-bar">
      <rect x="0" y="5" width="2" height="3" rx=".5" fill="#fff"/><rect x="3" y="3.5" width="2" height="4.5" rx=".5" fill="#fff"/>
      <rect x="6" y="2" width="2" height="6" rx=".5" fill="#fff"/><rect x="9" y=".5" width="2" height="7.5" rx=".5" fill="#fff"/>
      <path d="M14 3.2a6 6 0 0 1 8 0M15.5 5a3.6 3.6 0 0 1 5 0" stroke="#fff" stroke-width="1.1" fill="none" stroke-linecap="round"/>
      <circle cx="18" cy="7" r="1" fill="#fff"/>
      <rect x="24.5" y="1" width="11" height="6.5" rx="1.6" fill="none" stroke="#fff" stroke-opacity=".5"/>
      <rect x="25.7" y="2.2" width="8.6" height="4.1" rx=".8" fill="#fff"/>
    </g>
    <g id="step-tick">
      <circle cx="9" cy="9" r="7.5" fill="none" stroke="#6FCCEA" stroke-width="1.3"/>
      <path d="M5 9.2l3 3 6-7" fill="none" stroke="#6FCCEA" stroke-width="2" stroke-linecap="round" stroke-linejoin="round"/>
    </g>
    <g id="info">
      <circle cx="4.5" cy="4.5" r="4.5" fill="#fff"/><rect x="4" y="2" width="1.1" height="3.3" fill="#1d2126"/><rect x="4" y="6" width="1.1" height="1.1" fill="#1d2126"/>
    </g>
    <path id="chevron-right" d="M1 1l3 3-3 3" fill="none" stroke="#fff" stroke-width="1.4" stroke-linecap="round" stroke-linejoin="round"/>
    <path id="chevron-left" d="M5 1L1 5l4 4" fill="none" stroke="#fff" stroke-width="1.4" stroke-linecap="round" stroke-linejoin="round"/>
  </defs>
</svg>

<!-- Login -->
<section class="screen screen--login" aria-label="Login to your account">
  <span class="status-time">9:41</span>
  <svg class="status-icons" width="36" height="9"><use href="#status-bar"/></svg>
  <svg class="back" width="7" height="10"><use href="#chevron-left"/></svg>
  <h1 class="title">Login to your<br>account</h1>
  <div class="brand"><span class="brand-dot"></span>OurPlume</div>
  <div class="progress"><span></span><span></span></div>

  <div class="field field--filled" style="top:161px">
    <span class="icon-lead"><svg width="9" height="7"><rect width="9" height="7" rx="1" fill="#8d98a5"/><path d="M.5 .8L4.5 4l4-3.2" stroke="#2a3440" fill="none"/></svg></span>
    sample@plumemail.co<span class="caret"></span>
  </div>
  <div class="field field--filled" style="top:201px">
    <span class="icon-lead"><svg width="8" height="9"><rect y="3.5" width="8" height="5.5" rx="1" fill="#0094D4"/><path d="M2 4V2.5a2 2 0 0 1 4 0V4" stroke="#0094D4" fill="none" stroke-width="1.2"/></svg></span>
    <span class="mask">●●●●●●●●</span>
    <span class="icon-trail"><svg width="11" height="9"><path d="M1 4.5C3 1 8 1 10 4.5 8 8 3 8 1 4.5z" fill="none" stroke="#0094D4" stroke-width="1.1"/><circle cx="5.5" cy="4.5" r="1.5" fill="#0094D4"/><path d="M2 8.5L9 .5" stroke="#0094D4" stroke-width="1.1"/></svg></span>
  </div>
  <a class="link forgot">Forgot password?</a>
  <div class="button" style="top:267px">Join Now</div>
  <div class="divider">Or</div>
  <p class="scan-label">Sign in with Face Scan</p>
  <svg class="scan-icon" width="26" height="26" viewBox="0 0 26 26">
    <path d="M1 7V3a2 2 0 0 1 2-2h4M19 1h4a2 2 0 0 1 2 2v4M25 19v4a2 2 0 0 1-2 2h-4M7 25H3a2 2 0 0 1-2-2v-4" fill="none" stroke="#fff" stroke-width="1.3"/>
    <circle cx="13" cy="9.5" r="4" fill="#0677BA"/><path d="M5.5 21a7.5 6 0 0 1 15 0z" fill="#0677BA"/>
  </svg>
  <p class="signup-prompt">Don't have an account? <a class="link">Create an account</a></p>
</section>

<!-- Step 1: personal details -->
<section class="screen screen--details" aria-label="Create new account, personal details">
  <span class="status-time">9:41</span>
  <svg class="status-icons" width="36" height="9"><use href="#status-bar"/></svg>
  <svg class="back" width="7" height="10"><use href="#chevron-left"/></svg>
  <h1 class="title">Create new<br>account</h1>
  <div class="brand"><span class="brand-dot"></span>OurPlume</div>
  <div class="progress"><span></span><span></span></div>

  <div class="stepper">
    <span class="step-line" style="left:22px;width:60px"></span>
    <span class="step-line" style="left:94px;width:52px"></span>
    <span class="step-current" style="left:8px">1</span>
    <span class="step-idle" style="left:83px">2</span>
    <span class="step-idle" style="left:146px">3</span>
    <span class="step-label" style="left:-11px">Personal<br>details</span>
  </div>

  <p class="lead" style="top:223px">Enter your First/Last name and Date of Birth as<br>it appears on your government issued ID</p>
  <div class="field field--wide field--active" style="top:257px">Anvel<span class="caret"></span></div>
  <div class="field field--wide" style="top:296px">Last Name</div>
  <div class="field field--wide" style="top:335px">Date of Birth
    <span class="icon-trail"><svg width="9" height="9"><rect y="1.5" width="9" height="7.5" rx="1.2" fill="#0094D4"/><rect x="1" y="3.5" width="7" height="1" fill="#1e2b39"/><rect x="2" y="0" width="1" height="2.5" fill="#0094D4"/><rect x="6" y="0" width="1" height="2.5" fill="#0094D4"/></svg></span>
  </div>
  <div class="note note-inline"><svg width="9" height="9"><use href="#info"/></svg><span><strong>Note that:</strong> You must be 18 years old or over.</span></div>
  <div class="privacy">
    <span class="privacy-icon"><svg width="6" height="7"><rect y="2.8" width="6" height="4.2" rx=".8" fill="#fff"/><path d="M1.5 3V2a1.5 1.5 0 0 1 3 0v1" stroke="#fff" fill="none"/></svg></span>
    <span>We are committed to ensuring the privacy of your information. Please see our <a class="link">Privacy Policy</a></span>
  </div>
  <div class="button" style="top:449px">Next <svg width="6" height="8"><use href="#chevron-right"/></svg></div>
</section>

<!-- Step 2: username -->
<section class="screen screen--username" aria-label="Create new account, user name">
  <span class="status-time">9:41</span>
  <svg class="status-icons" width="36" height="9"><use href="#status-bar"/></svg>
  <svg class="back" width="7" height="10"><use href="#chevron-left"/></svg>
  <h1 class="title">Create new<br>account</h1>
  <div class="brand"><span class="brand-dot"></span>OurPlume</div>
  <div class="progress"><span></span><span></span></div>

  <div class="stepper">
    <span class="step-line step-line--done" style="left:20px;width:62px"></span>
    <span class="step-line" style="left:95px;width:55px"></span>
    <svg class="step-done" style="left:2px" width="18" height="18"><use href="#step-tick"/></svg>
    <span class="step-current" style="left:73px">2</span>
    <span class="step-idle" style="left:150px">3</span>
    <span class="step-label" style="left:54px">User name</span>
  </div>

  <p class="lead" style="top:214px">Create a unique OurPlume username</p>
  <div class="field field--wide" style="top:239px">User Name</div>
  <div class="note note-block" style="top:279px;height:79px">
    <div class="note-head"><svg width="9" height="9"><use href="#info"/></svg>Note that:</div>
    <p class="note-body">User name must be 3 to 20 characters long. Letters and numbers only. Special characters and spaces are not allowed.</p>
  </div>
  <div class="button" style="top:449px">Next <svg width="6" height="8"><use href="#chevron-right"/></svg></div>
</section>

<!-- Step 3: email and password -->
<section class="screen screen--credentials" aria-label="Create new account, email and password">
  <span class="status-time">9:41</span>
  <svg class="status-icons" width="36" height="9"><use href="#status-bar"/></svg>
  <svg class="back" width="7" height="10"><use href="#chevron-left"/></svg>
  <h1 class="title">Create new<br>account</h1>
  <div class="brand"><span class="brand-dot"></span>OurPlume</div>
  <div class="progress"><span></span><span></span></div>

  <div class="stepper">
    <span class="step-line step-line--done" style="left:20px;width:45px"></span>
    <span class="step-line step-line--done" style="left:84px;width:55px"></span>
    <svg class="step-done" style="left:2px" width="18" height="18"><use href="#step-tick"/></svg>
    <svg class="step-done" style="left:66px" width="18" height="18"><use href="#step-tick"/></svg>
    <span class="step-current" style="left:139px">3</span>
    <span class="step-label" style="left:120px">Email and<br>password</span>
  </div>

  <p class="lead" style="top:223px">Create your OurPlume login</p>
  <div class="field field--wide" style="top:247px">Email</div>
  <div class="field field--wide" style="top:286px">Password</div>
  <div class="note note-block" style="top:330px;height:89px">
    <div class="note-head"><svg width="9" height="9"><use href="#info"/></svg>Note that:</div>
    <p class="note-body">Password must be 8 Characters minimum. Must contain 1 uppercase character, 1 lowercase character, 1 numbers and 1 special character.</p>
  </div>
  <div class="button" style="top:449px">Next <svg width="6" height="8"><use href="#chevron-right"/></svg></div>
</section>

</body>
</html>
```